KORBALT

The business want a professional looking business card. We have a scetch we will add but want the extra upgrade, and would like more suggestions for variations of our business cards.

```html
<!DOCTYPE html>
<html lang="en">
<head>
<meta charset="utf-8">
<title>KORBALT Business Card</title>
<link href="https://fonts.googleapis.com/css2?family=Poppins:wght@300;400;500&display=swap" rel="stylesheet">
<style>
  :root {
    --backdrop: #d0c7bd;
    --card-dark: #323232;
    --card-light: #f9f3eb;
    --gold: #b89a5c;
    --ink: #2f2f2f;
  }
  * { margin: 0; padding: 0; box-sizing: border-box; }
  html, body {
    width: 1200px; height: 971px; overflow: hidden;
    background: var(--backdrop);
    font-family: "Poppins", sans-serif;
  }
  .canvas { position: relative; width: 1200px; height: 971px; }

  .card { position: absolute; left: 243px; width: 714px; height: 418px; overflow: hidden; }
  .card-front { top: 50px; background: var(--card-dark); }
  .card-back { top: 503px; display: flex; }

  .decor-area {
    position: absolute; right: 0; top: 0; width: 420px; height: 418px;
    background: radial-gradient(ellipse at 60% 50%, #3a3a3a 0%, #323232 55%, #2b2b2b 100%);
  }

  .brand {
    position: absolute; width: 300px; text-align: center; color: var(--gold);
  }
  .brand-dot {
    display: block; margin: 0 auto 22px; width: 46px; height: 46px;
    border-radius: 50%; background: var(--gold);
  }
  .brand-name {
    font-weight: 500; font-size: 40px; letter-spacing: 2px; line-height: 1;
  }
  .brand-since {
    margin-top: 14px; font-weight: 400; font-size: 11px; letter-spacing: 0.3px;
  }
  .card-front .brand { left: 21px; top: 140px; }

  .panel-info {
    position: relative; width: 418px; height: 418px; background: var(--card-light); color: var(--ink);
  }
  .panel-brand {
    position: relative; width: 296px; height: 418px; background: var(--card-dark);
  }
  .panel-brand .brand { left: -2px; top: 140px; }

  .person { position: absolute; top: 70px; left: 0; width: 422px; text-align: center; }
  .person-name { font-weight: 400; font-size: 31px; letter-spacing: 0.5px; line-height: 1; }
  .person-role { margin-top: 14px; font-size: 17px; letter-spacing: 3px; line-height: 1; }
  .person-full { margin-top: 11px; font-size: 13px; letter-spacing: 2px; font-weight: 300; }
  .rule { position: absolute; top: 164px; left: 163px; width: 88px; height: 1.5px; background: var(--gold); }

  .contacts { position: absolute; left: 46px; top: 205px; list-style: none; }
  .contact { display: flex; align-items: center; height: 52px; font-size: 19px; font-weight: 400; }
  .contact-icon { width: 24px; height: 24px; margin-right: 21px; flex: none; }
</style>
</head>
<body>
<div class="canvas">

  <section class="card card-front">
    <div class="decor-area" role="img" aria-label="Large faint tonal brand ornament"></div>
    <div class="brand">
      <span class="brand-dot"></span>
      <div class="brand-name">KORBALT</div>
      <div class="brand-since">SINCE 2026</div>
    </div>
  </section>

  <section class="card card-back">
    <div class="panel-info">
      <div class="person">
        <div class="person-name">KORBALT LINDRUP</div>
        <div class="person-role">CEO &amp; FOUNDER</div>
        <div class="person-full">Mats Aksel Lindrup</div>
      </div>
      <div class="rule"></div>
      <ul class="contacts">
        <li class="contact">
          <svg class="contact-icon" viewBox="0 0 24 34" fill="none" stroke="#2f2f2f" stroke-width="2">
            <rect x="3" y="1" width="18" height="32" rx="2"/>
            <line x1="3" y1="5" x2="21" y2="5"/><line x1="3" y1="29" x2="21" y2="29"/>
          </svg>
          004790554172
        </li>
        <li class="contact">
          <svg class="contact-icon" viewBox="0 0 24 18" fill="none" stroke="#2f2f2f" stroke-width="1.3">
            <rect x="1" y="1" width="22" height="16" rx="1"/>
            <polyline points="1,1 12,10 23,1"/><line x1="1" y1="17" x2="9" y2="8"/><line x1="23" y1="17" x2="15" y2="8"/>
          </svg>
          korbalt.llc@postmail.com
        </li>
        <li class="contact">
          <svg class="contact-icon" viewBox="0 0 24 24" fill="none" stroke="#2f2f2f" stroke-width="1.1">
            <circle cx="11" cy="11" r="10"/><ellipse cx="11" cy="11" rx="4.5" ry="10"/>
            <line x1="1" y1="11" x2="21" y2="11"/><line x1="11" y1="1" x2="11" y2="21"/>
            <path d="M3 6h16M3 16h16"/>
            <path d="M15 15l7 3-3 1-1 3z" fill="#2f2f2f"/>
          </svg>
          www.korbalt.llc
        </li>
      </ul>
    </div>
    <div class="panel-brand">
      <div class="brand">
        <span class="brand-dot"></span>
        <div class="brand-name">KORBALT</div>
        <div class="brand-since">SINCE 2026</div>
      </div>
    </div>
  </section>

</div>
</body>
</html>
```